College Social website needs a SIMPLE chart design

We need a simple one page website. The website is called "Brev-Onto" a phonetic spelling of the word collage. The site allows users to gain up to date information on the nightlife and social scene of the campus. The site must be able to easily convey several key pieces of information; some type of grid/chart would work well.

This includes:
primary information:
-The name of the bar (about 9 bars on campus)
-The length of the line
-Guy/Girl ratio
-If there is cover (admittance fee) to enter the bar

secondary information:
-how packed/full the bar is
-if there is police raiding the bar
-a way to show more information including drink specials

would prefer a design similar to this page except more colorful/playful/fun: http://m.quillbarrowreg.example/results.php
Updates

Some stylistic tips - the name of the service is called brev onto. a phonetic spelling of collage (http://en.fenwickpedia.example/wiki/Collage). it doesnt need to look like a rainbow, just be exciting, engaging, and vivid.

look at this page for reference: http://www.dravelnook.example/blog/flat-ui-design-showcase/

other than the bar name and drink specials, everything should be presented graphically. All the bar stats are approximations and rough estimates, so you must find a way to present the information as relatives. historical information is not relevant. only the real time stats need to be included. here is a sample:

Bar name: Sample bar
guy/girl ratio: 70/30
line length: short
admittance fee: yes
bar attendance: near full
police raid: no
drink specials:
WINE NIGHT!
$8 BOTTLES OF HALTERMOSS WINE
$8 BOTTLES OF CHAMPAGNE
$2 ZEM GOLD BOTTLES
$2 WELLS

Target Market(s)

target market for the site is 18-21 year olds in college.

Industry/Entity Type

College

Requirements
Must have
• the design MUST be mobile friendly. keep it simple. a flat design would be preferred.
the information must be conveyed in the form of symbols/icons. for instance, a pie chart to show guy/girl ratio.

```html
<!DOCTYPE html>
<html lang="en">
<head>
<meta charset="utf-8">
<title>Brev-Onto</title>
<link href="https://fonts.googleapis.com/css2?family=Alegreya+Sans:wght@400;500;700&family=Arimo:wght@400;700&display=swap" rel="stylesheet">
<style>
  :root {
    --ink: #262626;
    --red: #c8121a;
    --red-dark: #a80f15;
    --white: #ffffff;
    --ground: #f1f1f1;
    --seam: #e6e6e6;
    --idle: #d6d6d6;
  }
  * { box-sizing: border-box; margin: 0; padding: 0; }
  html, body { width: 864px; height: 1200px; overflow: hidden; }
  body {
    background: var(--ground);
    font-family: "Alegreya Sans", "Trebuchet MS", sans-serif;
    color: var(--ink);
    position: relative;
  }
  .site-header {
    height: 67px;
    background: var(--ink);
    display: flex; align-items: center; justify-content: center;
  }
  .brand {
    color: var(--white);
    font-weight: 500;
    font-size: 34px;
    letter-spacing: 0.5px;
  }
  .filter-bar {
    height: 34px;
    background: var(--red);
    color: var(--white);
    font-family: "Arimo", Arial, sans-serif;
    font-size: 19px;
    line-height: 34px;
    padding-left: 29px;
  }
  .bar-list { list-style: none; margin-top: 11px; }
  .bar-item {
    position: relative;
    height: 101px;
    margin-bottom: 4px;
    background: var(--white);
    display: flex; align-items: center;
    border-bottom: 1px solid var(--seam);
  }
  .bar-icon { width: 56px; height: 56px; margin-left: 20px; flex: none; }
  .bar-text { margin-left: 14px; margin-top: -6px; width: 250px; flex: none; }
  .bar-name { font-size: 21px; font-weight: 500; line-height: 1; }
  .bar-details {
    font-size: 14.5px; font-weight: 700; color: var(--red);
    margin-left: 13px; line-height: 1.1;
  }
  .bar-stats {
    display: flex; gap: 34px; align-items: center;
    margin-left: 40px;
  }
  .stat { width: 40px; height: 40px; display: block; }
  .stat .on { fill: var(--ink); }
  .stat .off { fill: var(--idle); }
  .stat .hot { fill: var(--red); }
  .pie-base { fill: var(--red); }
  .pie-slice { fill: none; stroke: var(--ink); stroke-width: 16; }
  .cover-ring { fill: none; stroke-width: 3; }
  .cover-yes .cover-ring { stroke: var(--red); }
  .cover-no .cover-ring { stroke: var(--idle); }
  .cover-sign { font-family: "Arimo", Arial, sans-serif; font-weight: 700; font-size: 20px; text-anchor: middle; }
  .cover-yes .cover-sign { fill: var(--red); }
  .cover-no .cover-sign { fill: var(--idle); }
  .cover-strike { stroke: var(--idle); stroke-width: 3; }
  .bar-expand {
    position: absolute; right: 0; top: 0;
    width: 108px; height: 100px;
  }
  .more-band {
    position: absolute; top: 1057px; left: 0; right: 0; height: 56px;
    display: flex; justify-content: center; align-items: center;
  }
  .more-button {
    width: 182px; height: 28px;
    background: var(--ink);
    border-left: 5px solid var(--red);
    border-right: 5px solid var(--red);
    color: var(--white);
    font-family: "Arimo", Arial, sans-serif;
    font-weight: 700; font-size: 19px;
    text-align: center; line-height: 28px;
  }
  .site-footer {
    position: absolute; top: 1113px; left: 0; right: 0; height: 64px;
    background: var(--ink);
    display: flex; align-items: center; justify-content: space-between;
    padding: 0 29px;
  }
  .contact { color: var(--white); font-size: 21px; font-weight: 700; }
  .social { display: flex; gap: 6px; }
  .social span { width: 27px; height: 27px; border-radius: 50%; background: var(--white); display: block; }
  .foot-strip {
    position: absolute; top: 1177px; left: 0; right: 0; height: 23px;
    background: var(--red-dark);
  }
</style>
</head>
<body>
  <header class="site-header"><span class="brand">Brev-Onto</span></header>
  <div class="filter-bar">Filters</div>

  <svg width="0" height="0" style="position:absolute">
    <defs>
      <symbol id="map-pin" viewBox="0 0 56 56">
        <path d="M3 16 L16 12 L28 16 L40 12 V50 L28 54 L16 50 L3 54 Z" fill="none" stroke="#000" stroke-width="3.5" stroke-linejoin="round"/>
        <path d="M16 12 V50 M28 16 V54" stroke="#000" stroke-width="3"/>
        <path d="M8 38 L16 32 L24 38 L34 30" fill="none" stroke="#000" stroke-width="2.5" stroke-dasharray="3 3"/>
        <path d="M44 2 C37 2 34 7 34 11 C34 17 44 26 44 26 C44 26 54 17 54 11 C54 7 51 2 44 2 Z" fill="#000"/>
        <circle cx="44" cy="11" r="3.5" fill="#fff"/>
      </symbol>
      <symbol id="expand-tab" viewBox="0 0 108 100">
        <polygon points="18,0 108,0 108,100 0,100" fill="#262626"/>
        <line x1="11" y1="0" x2="-5" y2="100" stroke="#262626" stroke-width="4"/>
        <rect x="61" y="40" width="4" height="22" fill="#c8121a"/>
        <rect x="52" y="49" width="22" height="4" fill="#c8121a"/>
      </symbol>
    </defs>
  </svg>

  <ul class="bar-list">
    <!-- row 1 -->
    <li class="bar-item"><svg class="bar-icon"><use href="#map-pin"/></svg><div class="bar-text"><div class="bar-name">The name of the bar</div><div class="bar-details">More details goes here</div></div>
      <div class="bar-stats">
        <svg class="stat" viewBox="0 0 40 40" role="img" aria-label="Guy/girl ratio 70/30"><circle class="pie-base" cx="20" cy="20" r="16"/><circle class="pie-slice" cx="20" cy="20" r="8" pathLength="100" stroke-dasharray="70 100" transform="rotate(-90 20 20)"/></svg>
        <svg class="stat" viewBox="0 0 40 40" role="img" aria-label="Line length short"><rect class="on" x="4" y="26" width="8" height="10"/><rect class="off" x="16" y="17" width="8" height="19"/><rect class="off" x="28" y="6" width="8" height="30"/></svg>
        <svg class="stat cover-yes" viewBox="0 0 40 40" role="img" aria-label="Cover charge"><circle class="cover-ring" cx="20" cy="20" r="16"/><text class="cover-sign" x="20" y="27">$</text></svg>
        <svg class="stat" viewBox="0 0 40 40" role="img" aria-label="Attendance near full"><rect class="on" x="2" y="12" width="6" height="16"/><rect class="on" x="10" y="12" width="6" height="16"/><rect class="on" x="18" y="12" width="6" height="16"/><rect class="hot" x="26" y="12" width="6" height="16"/><rect class="off" x="34" y="12" width="6" height="16"/></svg>
      </div>
      <svg class="bar-expand"><use href="#expand-tab"/></svg></li>
    <!-- row 2 -->
    <li class="bar-item"><svg class="bar-icon"><use href="#map-pin"/></svg><div class="bar-text"><div class="bar-name">The name of the bar</div><div class="bar-details">More details goes here</div></div>
      <div class="bar-stats">
        <svg class="stat" viewBox="0 0 40 40" role="img" aria-label="Guy/girl ratio 55/45"><circle class="pie-base" cx="20" cy="20" r="16"/><circle class="pie-slice" cx="20" cy="20" r="8" pathLength="100" stroke-dasharray="55 100" transform="rotate(-90 20 20)"/></svg>
        <svg class="stat" viewBox="0 0 40 40" role="img" aria-label="Line length medium"><rect class="on" x="4" y="26" width="8" height="10"/><rect class="on" x="16" y="17" width="8" height="19"/><rect class="off" x="28" y="6" width="8" height="30"/></svg>
        <svg class="stat cover-no" viewBox="0 0 40 40" role="img" aria-label="No cover charge"><circle class="cover-ring" cx="20" cy="20" r="16"/><text class="cover-sign" x="20" y="27">$</text><line class="cover-strike" x1="9" y1="31" x2="31" y2="9"/></svg>
        <svg class="stat" viewBox="0 0 40 40" role="img" aria-label="Attendance half full"><rect class="on" x="2" y="12" width="6" height="16"/><rect class="on" x="10" y="12" width="6" height="16"/><rect class="hot" x="18" y="12" width="6" height="16"/><rect class="off" x="26" y="12" width="6" height="16"/><rect class="off" x="34" y="12" width="6" height="16"/></svg>
      </div>
      <svg class="bar-expand"><use href="#expand-tab"/></svg></li>
    <!-- row 3 -->
    <li class="bar-item"><svg class="bar-icon"><use href="#map-pin"/></svg><div class="bar-text"><div class="bar-name">The name of the bar</div><div class="bar-details">More details goes here</div></div>
      <div class="bar-stats">
        <svg class="stat" viewBox="0 0 40 40" role="img" aria-label="Guy/girl ratio 40/60"><circle class="pie-base" cx="20" cy="20" r="16"/><circle class="pie-slice" cx="20" cy="20" r="8" pathLength="100" stroke-dasharray="40 100" transform="rotate(-90 20 20)"/></svg>
        <svg class="stat" viewBox="0 0 40 40" role="img" aria-label="Line length long"><rect class="on" x="4" y="26" width="8" height="10"/><rect class="on" x="16" y="17" width="8" height="19"/><rect class="hot" x="28" y="6" width="8" height="30"/></svg>
        <svg class="stat cover-yes" viewBox="0 0 40 40" role="img" aria-label="Cover charge"><circle class="cover-ring" cx="20" cy="20" r="16"/><text class="cover-sign" x="20" y="27">$</text></svg>
        <svg class="stat" viewBox="0 0 40 40" role="img" aria-label="Attendance full"><rect class="on" x="2" y="12" width="6" height="16"/><rect class="on" x="10" y="12" width="6" height="16"/><rect class="on" x="18" y="12" width="6" height="16"/><rect class="on" x="26" y="12" width="6" height="16"/><rect class="hot" x="34" y="12" width="6" height="16"/></svg>
      </div>
      <svg class="bar-expand"><use href="#expand-tab"/></svg></li>
    <!-- row 4 -->
    <li class="bar-item"><svg class="bar-icon"><use href="#map-pin"/></svg><div class="bar-text"><div class="bar-name">The name of the bar</div><div class="bar-details">More details goes here</div></div>
      <div class="bar-stats">
        <svg class="stat" viewBox="0 0 40 40" role="img" aria-label="Guy/girl ratio 60/40"><circle class="pie-base" cx="20" cy="20" r="16"/><circle class="pie-slice" cx="20" cy="20" r="8" pathLength="100" stroke-dasharray="60 100" transform="rotate(-90 20 20)"/></svg>
        <svg class="stat" viewBox="0 0 40 40" role="img" aria-label="Line length short"><rect class="on" x="4" y="26" width="8" height="10"/><rect class="off" x="16" y="17" width="8" height="19"/><rect class="off" x="28" y="6" width="8" height="30"/></svg>
        <svg class="stat cover-no" viewBox="0 0 40 40" role="img" aria-label="No cover charge"><circle class="cover-ring" cx="20" cy="20" r="16"/><text class="cover-sign" x="20" y="27">$</text><line class="cover-strike" x1="9" y1="31" x2="31" y2="9"/></svg>
        <svg class="stat" viewBox="0 0 40 40" role="img" aria-label="Attendance low"><rect class="hot" x="2" y="12" width="6" height="16"/><rect class="off" x="10" y="12" width="6" height="16"/><rect class="off" x="18" y="12" width="6" height="16"/><rect class="off" x="26" y="12" width="6" height="16"/><rect class="off" x="34" y="12" width="6" height="16"/></svg>
      </div>
      <svg class="bar-expand"><use href="#expand-tab"/></svg></li>
    <!-- row 5 -->
    <li class="bar-item"><svg class="bar-icon"><use href="#map-pin"/></svg><div class="bar-text"><div class="bar-name">The name of the bar</div><div class="bar-details">More details goes here</div></div>
      <div class="bar-stats">
        <svg class="stat" viewBox="0 0 40 40" role="img" aria-label="Guy/girl ratio 50/50"><circle class="pie-base" cx="20" cy="20" r="16"/><circle class="pie-slice" cx="20" cy="20" r="8" pathLength="100" stroke-dasharray="50 100" transform="rotate(-90 20 20)"/></svg>
        <svg class="stat" viewBox="0 0 40 40" role="img" aria-label="Line length medium"><rect class="on" x="4" y="26" width="8" height="10"/><rect class="on" x="16" y="17" width="8" height="19"/><rect class="off" x="28" y="6" width="8" height="30"/></svg>
        <svg class="stat cover-yes" viewBox="0 0 40 40" role="img" aria-label="Cover charge"><circle class="cover-ring" cx="20" cy="20" r="16"/><text class="cover-sign" x="20" y="27">$</text></svg>
        <svg class="stat" viewBox="0 0 40 40" role="img" aria-label="Attendance near full"><rect class="on" x="2" y="12" width="6" height="16"/><rect class="on" x="10" y="12" width="6" height="16"/><rect class="on" x="18" y="12" width="6" height="16"/><rect class="hot" x="26" y="12" width="6" height="16"/><rect class="off" x="34" y="12" width="6" height="16"/></svg>
      </div>
      <svg class="bar-expand"><use href="#expand-tab"/></svg></li>
    <!-- row 6 -->
    <li class="bar-item"><svg class="bar-icon"><use href="#map-pin"/></svg><div class="bar-text"><div class="bar-name">The name of the bar</div><div class="bar-details">More details goes here</div></div>
      <div class="bar-stats">
        <svg class="stat" viewBox="0 0 40 40" role="img" aria-label="Guy/girl ratio 65/35"><circle class="pie-base" cx="20" cy="20" r="16"/><circle class="pie-slice" cx="20" cy="20" r="8" pathLength="100" stroke-dasharray="65 100" transform="rotate(-90 20 20)"/></svg>
        <svg class="stat" viewBox="0 0 40 40" role="img" aria-label="Line length long"><rect class="on" x="4" y="26" width="8" height="10"/><rect class="on" x="16" y="17" width="8" height="19"/><rect class="hot" x="28" y="6" width="8" height="30"/></svg>
        <svg class="stat cover-yes" viewBox="0 0 40 40" role="img" aria-label="Cover charge"><circle class="cover-ring" cx="20" cy="20" r="16"/><text class="cover-sign" x="20" y="27">$</text></svg>
        <svg class="stat" viewBox="0 0 40 40" role="img" aria-label="Attendance full"><rect class="on" x="2" y="12" width="6" height="16"/><rect class="on" x="10" y="12" width="6" height="16"/><rect class="on" x="18" y="12" width="6" height="16"/><rect class="on" x="26" y="12" width="6" height="16"/><rect class="hot" x="34" y="12" width="6" height="16"/></svg>
      </div>
      <svg class="bar-expand"><use href="#expand-tab"/></svg></li>
    <!-- row 7 -->
    <li class="bar-item"><svg class="bar-icon"><use href="#map-pin"/></svg><div class="bar-text"><div class="bar-name">The name of the bar</div><div class="bar-details">More details goes here</div></div>
      <div class="bar-stats">
        <svg class="stat" viewBox="0 0 40 40" role="img" aria-label="Guy/girl ratio 45/55"><circle class="pie-base" cx="20" cy="20" r="16"/><circle class="pie-slice" cx="20" cy="20" r="8" pathLength="100" stroke-dasharray="45 100" transform="rotate(-90 20 20)"/></svg>
        <svg class="stat" viewBox="0 0 40 40" role="img" aria-label="Line length short"><rect class="on" x="4" y="26" width="8" height="10"/><rect class="off" x="16" y="17" width="8" height="19"/><rect class="off" x="28" y="6" width="8" height="30"/></svg>
        <svg class="stat cover-no" viewBox="0 0 40 40" role="img" aria-label="No cover charge"><circle class="cover-ring" cx="20" cy="20" r="16"/><text class="cover-sign" x="20" y="27">$</text><line class="cover-strike" x1="9" y1="31" x2="31" y2="9"/></svg>
        <svg class="stat" viewBox="0 0 40 40" role="img" aria-label="Attendance quiet"><rect class="on" x="2" y="12" width="6" height="16"/><rect class="hot" x="10" y="12" width="6" height="16"/><rect class="off" x="18" y="12" width="6" height="16"/><rect class="off" x="26" y="12" width="6" height="16"/><rect class="off" x="34" y="12" width="6" height="16"/></svg>
      </div>
      <svg class="bar-expand"><use href="#expand-tab"/></svg></li>
    <!-- row 8 -->
    <li class="bar-item"><svg class="bar-icon"><use href="#map-pin"/></svg><div class="bar-text"><div class="bar-name">The name of the bar</div><div class="bar-details">More details goes here</div></div>
      <div class="bar-stats">
        <svg class="stat" viewBox="0 0 40 40" role="img" aria-label="Guy/girl ratio 75/25"><circle class="pie-base" cx="20" cy="20" r="16"/><circle class="pie-slice" cx="20" cy="20" r="8" pathLength="100" stroke-dasharray="75 100" transform="rotate(-90 20 20)"/></svg>
        <svg class="stat" viewBox="0 0 40 40" role="img" aria-label="Line length medium"><rect class="on" x="4" y="26" width="8" height="10"/><rect class="on" x="16" y="17" width="8" height="19"/><rect class="off" x="28" y="6" width="8" height="30"/></svg>
        <svg class="stat cover-yes" viewBox="0 0 40 40" role="img" aria-label="Cover charge"><circle class="cover-ring" cx="20" cy="20" r="16"/><text class="cover-sign" x="20" y="27">$</text></svg>
        <svg class="stat" viewBox="0 0 40 40" role="img" aria-label="Attendance half full"><rect class="on" x="2" y="12" width="6" height="16"/><rect class="on" x="10" y="12" width="6" height="16"/><rect class="hot" x="18" y="12" width="6" height="16"/><rect class="off" x="26" y="12" width="6" height="16"/><rect class="off" x="34" y="12" width="6" height="16"/></svg>
      </div>
      <svg class="bar-expand"><use href="#expand-tab"/></svg></li>
    <!-- row 9 -->
    <li class="bar-item"><svg class="bar-icon"><use href="#map-pin"/></svg><div class="bar-text"><div class="bar-name">The name of the bar</div><div class="bar-details">More details goes here</div></div>
      <div class="bar-stats">
        <svg class="stat" viewBox="0 0 40 40" role="img" aria-label="Guy/girl ratio 35/65"><circle class="pie-base" cx="20" cy="20" r="16"/><circle class="pie-slice" cx="20" cy="20" r="8" pathLength="100" stroke-dasharray="35 100" transform="rotate(-90 20 20)"/></svg>
        <svg class="stat" viewBox="0 0 40 40" role="img" aria-label="Line length short"><rect class="on" x="4" y="26" width="8" height="10"/><rect class="off" x="16" y="17" width="8" height="19"/><rect class="off" x="28" y="6" width="8" height="30"/></svg>
        <svg class="stat cover-no" viewBox="0 0 40 40" role="img" aria-label="No cover charge"><circle class="cover-ring" cx="20" cy="20" r="16"/><text class="cover-sign" x="20" y="27">$</text><line class="cover-strike" x1="9" y1="31" x2="31" y2="9"/></svg>
        <svg class="stat" viewBox="0 0 40 40" role="img" aria-label="Attendance near full"><rect class="on" x="2" y="12" width="6" height="16"/><rect class="on" x="10" y="12" width="6" height="16"/><rect class="on" x="18" y="12" width="6" height="16"/><rect class="hot" x="26" y="12" width="6" height="16"/><rect class="off" x="34" y="12" width="6" height="16"/></svg>
      </div>
      <svg class="bar-expand"><use href="#expand-tab"/></svg></li>
  </ul>

  <div class="more-band"><div class="more-button">More ...</div></div>

  <footer class="site-footer">
    <span class="contact">Contact Us</span>
    <div class="social"><span></span><span></span></div>
  </footer>
  <div class="foot-strip"></div>
</body>
</html>
```